Need Business Card for our Real Estate Business with Sales Executive's Picture

PANTONE 484 C ( RED)

PANTONE 2766 C ( BLUE

Industry/Entity Type

Real Estate

Contact Information for Business Card

Name, Mobile, email, & picture of Person
Agency Phone, address, Web address

Requirements
Must have
• Our Logo Colours, Agent Picture,

```html
<!DOCTYPE html>
<html lang="en">
<head>
<meta charset="utf-8">
<title>Halvern Real Estate – Business Card</title>
<link rel="stylesheet" href="https://fonts.googleapis.com/css2?family=Cinzel:wght@500;600&family=PT+Sans:wght@400&display=swap">
<style>
  :root {
    --navy: #141b4d;
    --red: #9a3324;
    --ink: #2b2b33;
    --card: #ffffff;
    --stage: #e9e8ec;
    --photo-top: #e6e7ec;
    --photo-mid: #b98d78;
    --photo-low: #2b4a9a;
  }
  * { margin: 0; padding: 0; box-sizing: border-box; }
  html, body { width: 1200px; height: 844px; overflow: hidden; }
  body {
    background: var(--stage);
    display: flex;
    align-items: center;
    justify-content: center;
    gap: 60px;
    font-family: "PT Sans", Arial, sans-serif;
  }
  .card {
    width: 520px;
    height: 298px;
    background: var(--card);
    box-shadow: 0 6px 20px rgba(0,0,0,0.15);
    position: relative;
    overflow: hidden;
  }
  /* front */
  .agent-photo {
    position: absolute;
    left: 0; bottom: 0;
    width: 250px; height: 270px;
    background: linear-gradient(180deg, var(--photo-top) 0%, var(--photo-mid) 40%, var(--photo-low) 75%, #1f3a85 100%);
    border-top-right-radius: 4px;
  }
  .agent-details {
    position: absolute;
    left: 278px; top: 64px;
    color: var(--ink);
  }
  .agent-name {
    font-family: "Cinzel", Georgia, serif;
    font-weight: 600;
    font-size: 19px;
    letter-spacing: 0.5px;
    margin-bottom: 10px;
  }
  .agent-name .first { color: var(--navy); }
  .agent-name .last { color: var(--red); }
  .contact-list { list-style: none; font-size: 13.5px; line-height: 20px; }
  .contact-list li { display: flex; align-items: center; gap: 8px; }
  .contact-list svg { width: 11px; height: 11px; fill: var(--navy); flex: none; }
  .address { margin-top: 8px; font-size: 13.5px; line-height: 19px; color: var(--ink); }
  /* back */
  .brand {
    position: absolute;
    inset: 0;
    display: flex;
    align-items: center;
    justify-content: center;
    gap: 10px;
  }
  .brand-mark { width: 12px; height: 12px; background: var(--red); }
  .brand-name {
    font-family: "Cinzel", Georgia, serif;
    font-weight: 600;
    font-size: 30px;
    color: var(--navy);
    letter-spacing: 1px;
  }
</style>
</head>
<body>
  <section class="card card-front">
    <div class="agent-photo" role="img" aria-label="Portrait photo of the sales executive in a blue suit"></div>
    <div class="agent-details">
      <h1 class="agent-name"><span class="first">Marcus</span> <span class="last">Ellery</span></h1>
      <ul class="contact-list">
        <li><svg viewBox="0 0 24 24"><path d="M6.6 10.8a15 15 0 0 0 6.6 6.6l2.2-2.2a1 1 0 0 1 1-.25 11.4 11.4 0 0 0 3.6.57 1 1 0 0 1 1 1V20a1 1 0 0 1-1 1A17 17 0 0 1 3 4a1 1 0 0 1 1-1h3.5a1 1 0 0 1 1 1 11.4 11.4 0 0 0 .57 3.6 1 1 0 0 1-.25 1z"/></svg>052-418 730 226</li>
        <li><svg viewBox="0 0 24 24"><path d="M7 1h10a2 2 0 0 1 2 2v18a2 2 0 0 1-2 2H7a2 2 0 0 1-2-2V3a2 2 0 0 1 2-2zm0 3v14h10V4zm5 15.5a1 1 0 1 0 0 2 1 1 0 0 0 0-2z"/></svg>052-418 730 227</li>
        <li><svg viewBox="0 0 24 24"><path d="M2 5h20v14H2zm2 2v.5l8 5 8-5V7z"/></svg>hello@halvernhomes.com</li>
        <li><svg viewBox="0 0 24 24"><circle cx="12" cy="12" r="10"/></svg>www.halvernhomes.com</li>
      </ul>
      <p class="address">48 Cedar Row, Brookfield<br>Westland, 560217.</p>
    </div>
  </section>
  <section class="card card-back">
    <div class="brand">
      <span class="brand-mark"></span>
      <span class="brand-name">Halvern Real Estate</span>
    </div>
  </section>
</body>
</html>
```